Heart Gambit Shadow Reckoning - Movie Poster

I am an independent filmmaker and I would like a movie poster designed for my latest project, Heart Gambit - Shadow Reckoning. It's a dramatic, romantic spy movie. The synopsis is Desmond Pell and Greta Holloway retired from the NBX in order to live an ordinary suburban life in Germany. Greta secretly continued to accept missions with the agency. When Greta is kidnapped by Vadik, a vicious Russian killer, Desmond is desperate to save her before it is too late.

I've taken four pictures of the lead actors for the movie posters. Use the images in whatever way works best. I am looking forward to your movie poster designs.

Industry/Entity Type

Movie

Requirements
Must have
• Text that must be present on the poster:
• Heart Gambit - Shadow Reckoning
• A Marisol Quayle film
• When Greta is kidnapped, retired agent Desmond Pell will do anything to rescue her, but can he save her before it is too late?
• Brackwater Picture House presents a Marisol Quayle film Starring Marisol Quayle Tarun Velagiri Pete Grover Elian Baptiste Lon Tavish Helena Fisk Margaret Lyle Zandrea Cobbins Everett Ladislaw Tiffa Dunmore Lucia Bramante Greta Bramante Frankie Bramante Marguerite Talvic Ardit Velaj Caleb Pruett Dalton Ferrick Gordon Ashby Brent Lomax Vincent Treno Lamont Briggs Brenda Olcott Renzo Quarles Keith Yalmadian Valentina Ashby Glenn Perrault Curtis Vale Marlon Fitch Wade Pelletier Quincy Dorsett ORIGINAL SCORE BY Renata Voltri
Nice to have
• I would really like to emphasis the romance between the couple but also the violence of being a spy. It is okay to add images to accomplish this goal.

```html
<!DOCTYPE html>
<html lang="en">
<head>
<meta charset="utf-8">
<title>Heart Gambit - Shadow Reckoning</title>
<link rel="stylesheet" href="https://fonts.googleapis.com/css2?family=Montserrat:ital,wght@0,400;0,500;1,500&family=Oswald:wght@500;600&family=Rye&display=swap">
<style>
  :root {
    --ink: #050507;
    --white: #ffffff;
    --steel: #2a67b0;
    --steel-mid: #17427e;
    --steel-deep: #0a1c38;
    --ember: #e0843a;
    --ember-hot: #c4461c;
    --ember-deep: #5e1f0c;
    --plaid-red: #9a3a3e;
    --plaid-light: #c9b7bd;
    --shirt-black: #151218;
    --skin: #a0705a;
    --sequin: #2a2226;
    --title-orange: #e27b2f;
    --rule: #55555c;
    --credit: #d8d8dc;
  }
  * { margin: 0; padding: 0; box-sizing: border-box; }
  html, body { width: 776px; height: 1200px; overflow: hidden; background: var(--ink); }
  .poster {
    position: relative;
    width: 776px;
    height: 1200px;
    overflow: hidden;
    background: var(--ink);
    color: var(--white);
  }
  .scene { position: absolute; }
  .scene--ballroom {
    left: 0; top: 0; width: 388px; height: 640px;
    background: linear-gradient(180deg, var(--steel-mid) 0%, var(--steel) 30%, var(--steel-mid) 60%, var(--steel-deep) 82%, var(--ink) 100%);
  }
  .scene--couple-night {
    left: 388px; top: 0; width: 388px; height: 700px;
    background: linear-gradient(180deg, var(--ember-hot) 0%, var(--ember) 22%, #a94a1e 45%, var(--ember-deep) 70%, var(--ink) 100%);
  }
  .scene--lead-agent {
    left: 150px; top: 70px; width: 620px; height: 700px;
    border-radius: 46% 46% 12% 12% / 30% 30% 8% 8%;
    background:
      radial-gradient(ellipse 24% 20% at 58% 30%, var(--skin) 0%, #6e4a3c 70%, rgba(0,0,0,0) 100%),
      linear-gradient(120deg, var(--plaid-light) 0%, var(--plaid-red) 30%, var(--shirt-black) 48%, var(--shirt-black) 60%, var(--plaid-red) 78%, var(--plaid-light) 100%);
  }
  .scene--lead-woman {
    left: 190px; top: 440px; width: 586px; height: 400px;
    border-radius: 40% 10% 0 30%;
    background:
      radial-gradient(ellipse 22% 26% at 66% 22%, #7a5040 0%, rgba(0,0,0,0) 100%),
      linear-gradient(160deg, #1a1418 0%, var(--sequin) 40%, #120e12 75%, var(--ink) 100%);
  }
  .shade {
    position: absolute; left: 0; right: 0; bottom: 0; height: 480px;
    background: linear-gradient(180deg, rgba(5,5,7,0) 0%, rgba(5,5,7,0.7) 25%, var(--ink) 55%);
  }
  .credit-top {
    position: absolute; top: 20px; left: 0; width: 776px;
    text-align: center;
    font-family: "Montserrat", sans-serif;
    font-weight: 400;
    font-size: 23px;
    letter-spacing: 10px;
    text-transform: uppercase;
  }
  .tagline {
    position: absolute; top: 812px; left: 170px; width: 436px;
    text-align: center;
    font-family: "Oswald", sans-serif;
    font-weight: 500;
    font-size: 16px;
    line-height: 22px;
    letter-spacing: 1px;
    text-transform: uppercase;
  }
  .title {
    position: absolute; left: 0; width: 776px; text-align: center; display: block;
  }
  .title__main {
    top: 868px;
    font-family: "Montserrat", sans-serif;
    font-style: italic;
    font-weight: 500;
    font-size: 64px;
    letter-spacing: 1px;
    text-transform: uppercase;
  }
  .title__sub {
    top: 950px;
    font-family: "Rye", serif;
    font-size: 60px;
    color: var(--title-orange);
    text-transform: uppercase;
  }
  .rule {
    position: absolute; top: 1085px; left: 130px; width: 540px; height: 1px;
    background: var(--rule);
  }
  .billing {
    position: absolute; top: 1103px; left: 0; width: 776px;
    text-align: center;
    font-family: "Montserrat", sans-serif;
    font-weight: 500;
    font-size: 11.5px;
    letter-spacing: 1.2px;
    text-transform: uppercase;
  }
  .cast {
    position: absolute; top: 1128px; left: 40px; width: 696px;
    font-family: "Oswald", sans-serif;
    font-weight: 500;
    font-size: 8px;
    line-height: 15px;
    color: var(--credit);
    text-transform: uppercase;
    letter-spacing: 0.3px;
  }
  .cast__row { display: flex; justify-content: center; gap: 9px; white-space: nowrap; }
</style>
</head>
<body>
<main class="poster">
  <div class="scene scene--ballroom" role="img" aria-label="Blue-toned ballroom with a masked man in a tuxedo and guests around a table"></div>
  <div class="scene scene--couple-night" role="img" aria-label="Warm orange-toned photo of the couple smiling together at night"></div>
  <div class="scene scene--lead-agent" role="img" aria-label="The agent in a red plaid shirt over a black tee, pointing a pistol forward"></div>
  <div class="scene scene--lead-woman" role="img" aria-label="The woman in a black sequined dress lying back in his arms, gazing up at him"></div>
  <div class="shade"></div>

  <p class="credit-top">A Marisol Quayle Film</p>

  <p class="tagline">When Greta is kidnapped, retired agent Desmond Pell will do anything to rescue her, but can he save her before it is too late?</p>

  <h1>
    <span class="title title__main">Heart Gambit</span>
    <span class="title title__sub">Shadow Reckoning</span>
  </h1>

  <div class="rule"></div>

  <p class="billing">Brackwater Picture House presents a Marisol Quayle film starring</p>

  <div class="cast">
    <div class="cast__row"><span>Marisol Quayle</span><span>Tarun Velagiri</span><span>Pete Grover</span><span>Elian Baptiste</span><span>Lon Tavish</span><span>Helena Fisk</span><span>Margaret Lyle</span><span>Zandrea Cobbins</span><span>Everett Ladislaw</span><span>Tiffa Dunmore</span></div>
    <div class="cast__row"><span>Lucia Bramante</span><span>Greta Bramante</span><span>Frankie Bramante</span><span>Marguerite Talvic</span><span>Ardit Velaj</span><span>Caleb Pruett</span><span>Dalton Ferrick</span><span>Gordon Ashby</span><span>Brent Lomax</span><span>Vincent Treno</span><span>Lamont Briggs</span></div>
    <div class="cast__row"><span>Brenda Olcott</span><span>Renzo Quarles</span><span>Keith Yalmadian</span><span>Valentina Ashby</span><span>Glenn Perrault</span><span>Curtis Vale</span><span>Marlon Fitch</span><span>Wade Pelletier</span><span>Quincy Dorsett</span><span>Original Score by Renata Voltri</span></div>
  </div>
</main>
</body>
</html>
```